Valkemo App for Smart Devices IoT WiFi Electronic

Valkemo is a siren manufacturer. This application is used for the company's products that have a Wi-Fi connection and an internet connection, which can be configured and activated remotely through this application. In addition, this application is used to activate the siren at specific times for the start and end of shifts in companies and schools. Users will be siren installers and IT or HR managers.
In addition to activating motorized sirens timers, some siren models have speakers and allow you to play TTS (text to speech) audio, audio recorded by the user on the phone and upload audio (mp3) with playlist programming with start and end times.
Application screens: home with dashboard (one dashboard for each category). Device categories: timers, speakers, motorized siren. Screen for requesting evaluation in the Play Store. Screen for registering the user profile. Screen for registering devices according to their category (timers, speakers, motorized siren). Screen for registering device groups. Screen for pairing the device on the client's Wi-Fi network. Screen for registering activation times. Screen for uploading MP3 audios. Screen for registering playlists with audio selection, start and end times. Screen for recording audio for later sending to the speakers. Screen for converting text to speech and sending to the speakers. It is important to have a time picker with the day of the week to program the activation times and playlist.

Target Market(s)

Schools, Companies and Stores.

Industry/Entity Type

IoT

Font styles to use
Sans Serif
Other font styles liked:
• roboto

Colors
FFC000
F8CF3A
FAE287
FDF2CF
FEFAEE

Requirements
Must have
• time picker with weekdays for timer programming feature.
Nice to have
• app review request screen on play store

```html
<!DOCTYPE html>
<html lang="en">
<head>
<meta charset="utf-8">
<title>Valkemo – Siren App Screens</title>
<link href="https://fonts.googleapis.com/css2?family=Roboto:wght@400;500;700&display=swap" rel="stylesheet">
<style>
:root{
  --yellow:#FFC000;
  --gold:#F8CF3A;
  --sand:#FAE287;
  --cream:#FDF2CF;
  --ivory:#FEFAEE;
  --band:#FFD552;
  --white:#FFFFFF;
  --ink:#1E1E1E;
  --muted:#555555;
  --line:#E4E4E4;
  --icon:#6B6B6B;
}
*{box-sizing:border-box;margin:0;padding:0}
html,body{width:1200px;height:657px;overflow:hidden}
body{font-family:"Roboto",sans-serif;color:var(--ink);background:var(--yellow);position:relative}
.backdrop{position:absolute;inset:0;width:1200px;height:657px}
.phone{position:absolute;width:228px;height:503px;background:var(--white);border-radius:18px;overflow:hidden}
.phone > *{position:absolute}
.status-time{top:10px;left:17px;font-size:7.5px;font-weight:700}
.status-icons{top:10px;right:18px;width:38px;height:9px}
.brand{top:33px;left:16px;font-size:18px;font-weight:500;color:var(--yellow);letter-spacing:.2px}
.top-actions{top:35px;right:14px;display:flex;gap:4px}
.round-btn{width:17px;height:17px;border-radius:50%;background:var(--cream);display:flex;align-items:center;justify-content:center}
.round-btn svg{width:9px;height:9px}
.screen-title{left:0;width:100%;text-align:center;font-size:10px;font-weight:500}
.shift-card{top:87px;left:16px;width:195px;height:40px;background:var(--yellow);border-radius:4px;color:var(--white);padding:9px 0 0 29px}
.shift-card .badge{position:absolute;left:8px;top:12px;width:15px;height:15px;border-radius:50%;background:var(--white);display:flex;align-items:center;justify-content:center}
.shift-card h3{font-size:7.5px;font-weight:700}
.shift-card p{font-size:7px;margin-top:4px}
.switch{width:20px;height:10px;border-radius:5px;position:relative}
.switch::after{content:"";position:absolute;top:2px;width:6px;height:6px;border-radius:50%}
.switch.on{background:var(--white)}
.switch.on::after{right:2px;background:var(--yellow)}
.switch.off{border:1px solid #BDBDBD;background:var(--white)}
.switch.off::after{left:2px;top:1px;background:var(--yellow)}
.shift-card .switch{position:absolute;right:10px;top:10px;background:var(--white)}
.section-head{left:16px;width:195px;display:flex;justify-content:space-between;align-items:center;font-size:10px;font-weight:500}
.section-head .add{font-size:14px;font-weight:400}
.schedule{left:16px;width:195px;border:1px solid var(--line);border-radius:4px;padding:5px 10px 0 10px}
.schedule .time{font-size:7.5px;font-weight:700}
.schedule .days{font-size:4.5px;color:var(--yellow);font-weight:400;margin-left:3px}
.schedule .name{font-size:7px;color:var(--muted);margin-top:4px}
.schedule.first .name{color:var(--ink)}
.schedule .tools{position:absolute;right:11px;top:6px;display:flex;flex-direction:column;gap:5px}
.schedule .tools svg{width:6px;height:6px}
.schedule .audio{border-top:1px solid var(--line);margin-top:5px;padding-top:5px}
.schedule .audio b{display:block;font-size:7px;font-weight:400}
.schedule .audio span{display:block;font-size:5.5px;margin-top:2px}
.status-block{left:25px;top:396px;width:190px}
.status-block h4{font-size:9.5px;font-weight:500;display:flex;align-items:center;gap:4px}
.status-block h4 i{width:8px;height:8px;border-radius:50%;border:1.5px solid var(--yellow);display:inline-flex;align-items:center;justify-content:center}
.status-block h4 i::after{content:"";width:3px;height:3px;border-radius:50%;background:var(--yellow)}
.status-block p{font-size:7.5px;color:var(--muted);line-height:12px;margin:4px 0 0 13px}
.tab-bar{left:0;bottom:0;width:100%;height:37px;border-top:1px solid #F0F0F0;box-shadow:0 -1px 3px rgba(0,0,0,.04)}
.tab-bar .active-mark{position:absolute;left:17px;top:-1px;width:19px;height:2px;background:var(--yellow)}
.tab-bar svg{position:absolute;top:12px;width:12px;height:12px}
.field-label{left:16px;font-size:7px}
.field{left:16px;width:195px;height:25px;border:1px solid var(--line);border-radius:4px;font-size:6px;color:var(--muted);padding:0 10px;display:flex;align-items:center;justify-content:space-between}
.field .trail{width:13px;height:13px;border-radius:50%;background:var(--cream);display:flex;align-items:center;justify-content:center}
.field .trail svg{width:6px;height:6px}
.week-row{left:16px;top:258px;width:195px;display:flex;align-items:center;justify-content:space-between}
.week-row strong{font-size:9.5px;font-weight:500}
.week-row .choice{display:flex;align-items:center;gap:5px;font-size:5.5px}
.dropdown-list{left:16px;top:322px;width:195px;height:43px;border:1px solid var(--line);border-radius:4px;padding:5px 4px}
.dropdown-list div{font-size:6px;padding:0 6px;height:15px;line-height:15px}
.dropdown-list .hl{background:#F3F3F3;border-radius:2px}
.fab{left:103px;top:434px;width:22px;height:22px;border-radius:50%;background:var(--yellow);color:var(--ink);font-size:13px;display:flex;align-items:center;justify-content:center}
.device{left:16px;width:195px;height:25px;border:1px solid var(--line);border-radius:4px;display:flex;align-items:center;justify-content:space-between;padding:0 10px;font-size:6px}
.pair-text{left:30px;top:208px;font-size:10px;font-weight:500;line-height:16px}
.pair-link{left:29px;top:256px;width:170px;height:36px}
.pair-node{position:absolute;top:0;width:36px;height:36px;border-radius:50%;background:var(--cream);display:flex;align-items:center;justify-content:center}
.pair-node svg{width:10px;height:10px}
.pair-line{position:absolute;left:38px;right:38px;top:18px;border-top:1px dashed #555}
</style>
</head>
<body>

<svg class="backdrop" viewBox="0 0 1200 657" aria-hidden="true">
  <polygon points="0,0 748,0 1200,560 1200,657 520,657 0,12" fill="var(--band)"/>
  <polygon points="748,0 1200,0 1200,560" fill="var(--yellow)"/>
</svg>

<svg width="0" height="0" style="position:absolute">
  <defs>
    <symbol id="i-wifi" viewBox="0 0 24 24"><path d="M2 9a15 15 0 0 1 20 0l-2 2a12 12 0 0 0-16 0z M6 13a9 9 0 0 1 12 0l-2 2a6 6 0 0 0-8 0z" fill="#222"/><circle cx="12" cy="18" r="2.2" fill="#222"/></symbol>
    <symbol id="i-grid" viewBox="0 0 24 24"><g fill="#222"><rect x="3" y="3" width="5" height="5"/><rect x="10" y="3" width="5" height="5"/><rect x="17" y="3" width="5" height="5"/><rect x="3" y="10" width="5" height="5"/><rect x="10" y="10" width="5" height="5"/><rect x="17" y="10" width="5" height="5"/><rect x="3" y="17" width="5" height="5"/><rect x="10" y="17" width="5" height="5"/><rect x="17" y="17" width="5" height="5"/></g></symbol>
    <symbol id="i-user" viewBox="0 0 24 24"><circle cx="12" cy="7" r="5" fill="currentColor"/><path d="M3 22a9 8 0 0 1 18 0z" fill="currentColor"/></symbol>
    <symbol id="i-clock" viewBox="0 0 24 24"><circle cx="12" cy="12" r="9" fill="none" stroke="currentColor" stroke-width="3"/><path d="M12 7v6h4" fill="none" stroke="currentColor" stroke-width="3"/></symbol>
    <symbol id="i-pen" viewBox="0 0 24 24"><path d="M3 21l2-7 12-12 5 5-12 12z" fill="#222"/></symbol>
    <symbol id="i-home" viewBox="0 0 24 24"><path d="M12 2L1 12h3v10h16V12h3z" fill="var(--yellow)"/></symbol>
    <symbol id="i-box" viewBox="0 0 24 24"><rect x="2" y="3" width="20" height="5" fill="var(--icon)"/><rect x="3" y="9" width="18" height="13" fill="var(--icon)"/><rect x="9" y="12" width="6" height="2" fill="#fff"/></symbol>
    <symbol id="i-cal" viewBox="0 0 24 24"><rect x="2" y="3" width="20" height="19" rx="2" fill="var(--icon)"/><g fill="#fff"><rect x="5" y="9" width="3" height="3"/><rect x="10.5" y="9" width="3" height="3"/><rect x="16" y="9" width="3" height="3"/><rect x="5" y="15" width="3" height="3"/><rect x="10.5" y="15" width="3" height="3"/><rect x="16" y="15" width="3" height="3"/></g></symbol>
    <symbol id="i-gear" viewBox="0 0 24 24"><circle cx="12" cy="12" r="8" fill="none" stroke="var(--icon)" stroke-width="4" stroke-dasharray="3.5 2.8"/><circle cx="12" cy="12" r="6.5" fill="var(--icon)"/><circle cx="12" cy="12" r="3" fill="#fff"/></symbol>
    <symbol id="i-status" viewBox="0 0 38 9"><g fill="#222"><rect x="0" y="6" width="2" height="3"/><rect x="3" y="4" width="2" height="5"/><rect x="6" y="2" width="2" height="7"/><rect x="9" y="0" width="2" height="9"/><path d="M14 3a8 8 0 0 1 11 0l-1.5 1.5a6 6 0 0 0-8 0z M17 6a4 4 0 0 1 5 0l-2.5 3z"/><rect x="28" y="1.5" width="9" height="6" rx="1.2" fill="none" stroke="#222"/><rect x="29.5" y="3" width="5.5" height="3"/></g></symbol>
    <symbol id="i-caret" viewBox="0 0 24 24"><path d="M5 8h14l-7 8z" fill="#222"/></symbol>
    <symbol id="i-upload" viewBox="0 0 24 24"><path d="M12 2l7 8h-4v6H9v-6H5z M4 19h16v3H4z" fill="#222"/></symbol>
    <symbol id="i-radio" viewBox="0 0 24 24"><circle cx="12" cy="12" r="2.5" fill="#222"/><path d="M7 7a7 7 0 0 0 0 10 M17 7a7 7 0 0 1 0 10 M4 4a11 11 0 0 0 0 16 M20 4a11 11 0 0 1 0 16" fill="none" stroke="#222" stroke-width="1.8"/></symbol>
  </defs>
</svg>

<!-- Screen: schedules dashboard -->
<section class="phone" style="left:61px;top:55px">
  <span class="status-time">9:41</span>
  <svg class="status-icons"><use href="#i-status"/></svg>
  <span class="brand">valkemo</span>
  <div class="top-actions">
    <span class="round-btn"><svg><use href="#i-wifi"/></svg></span>
    <span class="round-btn"><svg><use href="#i-grid"/></svg></span>
    <span class="round-btn" style="color:#222"><svg><use href="#i-user"/></svg></span>
  </div>
  <h1 class="screen-title" style="top:67px">Motorized Sirens Timers</h1>
  <div class="shift-card">
    <span class="badge"><svg width="9" height="9"><use href="#i-radio"/></svg></span>
    <h3>Shift Timing</h3>
    <p>Activate the device for shift timing</p>
    <span class="switch on"></span>
  </div>
  <div class="section-head" style="top:140px"><span>Schedules</span><span class="add">+</span></div>

  <article class="schedule first" style="top:164px;height:58px">
    <div class="time">9am - 1pm<span class="days">Weekdays</span></div>
    <div class="name">1half session</div>
    <div class="audio"><b>Audio : Text to speech</b><span>The shift has be started, Have a nice day</span></div>
    <div class="tools"><svg style="color:#222"><use href="#i-clock"/></svg><svg><use href="#i-pen"/></svg></div>
  </article>
  <article class="schedule" style="top:229px;height:33px">
    <div class="time">1pm - 2pm<span class="days">Weekdays</span></div>
    <div class="name">Lunch Time</div>
    <div class="tools"><svg style="color:#222"><use href="#i-clock"/></svg><svg><use href="#i-pen"/></svg></div>
  </article>
  <article class="schedule" style="top:270px;height:33px">
    <div class="time">4pm - 4.20pm<span class="days">Weekdays</span></div>
    <div class="name">Coffee break</div>
    <div class="tools"><svg style="color:#222"><use href="#i-clock"/></svg><svg><use href="#i-pen"/></svg></div>
  </article>
  <article class="schedule" style="top:311px;height:33px">
    <div class="time">6pm<span class="days">Weekdays</span></div>
    <div class="name">Signing out time</div>
    <div class="tools"><svg style="color:#222"><use href="#i-clock"/></svg><svg><use href="#i-pen"/></svg></div>
  </article>
  <article class="schedule" style="top:352px;height:33px">
    <div class="time">9am - 12pm<span class="days">Weekdays</span></div>
    <div class="name">Special session</div>
    <div class="tools"><svg style="color:#222"><use href="#i-clock"/></svg><svg><use href="#i-pen"/></svg></div>
  </article>

  <div class="status-block">
    <h4><i></i>Status</h4>
    <p>Next Ring of siren is at 1:00pm to 2:00pm which is lunch time (siren alarm in 20 mins)</p>
  </div>

  <nav class="tab-bar">
    <span class="active-mark"></span>
    <svg style="left:21px"><use href="#i-home"/></svg>
    <svg style="left:77px"><use href="#i-box"/></svg>
    <svg style="left:140px"><use href="#i-cal"/></svg>
    <svg style="left:196px"><use href="#i-gear"/></svg>
  </nav>
</section>

<!-- Screen: add schedule -->
<section class="phone" style="left:343px;top:97px">
  <span class="status-time">9:41</span>
  <svg class="status-icons"><use href="#i-status"/></svg>
  <span class="brand">valkemo</span>
  <div class="top-actions">
    <span class="round-btn"><svg><use href="#i-wifi"/></svg></span>
    <span class="round-btn"><svg><use href="#i-grid"/></svg></span>
    <span class="round-btn" style="color:#222"><svg><use href="#i-user"/></svg></span>
  </div>
  <h1 class="screen-title" style="top:75px">Add the new schedules for siren</h1>

  <label class="field-label" style="top:100px">Title of siren alarm</label>
  <div class="field" style="top:113px">Enter</div>
  <label class="field-label" style="top:152px">Start time of siren</label>
  <div class="field" style="top:164px">Time</div>
  <label class="field-label" style="top:204px">End time of siren</label>
  <div class="field" style="top:216px">Time</div>

  <div class="week-row">
    <strong>Week :</strong>
    <span class="choice">Weekdays <span class="switch off"></span> Weekend</span>
  </div>

  <label class="field-label" style="top:283px">Audio Format</label>
  <div class="field" style="top:296px">MP3 Audio<span class="trail"><svg><use href="#i-caret"/></svg></span></div>
  <div class="dropdown-list">
    <div>Text to speech</div>
    <div class="hl">Audio Recordina</div>
  </div>

  <label class="field-label" style="top:372px">Choose audio from files</label>
  <label class="field-label" style="top:387px">MP3 Audio</label>
  <div class="field" style="top:400px">Choose audio from files<span class="trail"><svg><use href="#i-upload"/></svg></span></div>

  <span class="fab">+</span>

  <nav class="tab-bar">
    <span class="active-mark"></span>
    <svg style="left:21px"><use href="#i-home"/></svg>
    <svg style="left:77px"><use href="#i-box"/></svg>
    <svg style="left:140px"><use href="#i-cal"/></svg>
    <svg style="left:196px"><use href="#i-gear"/></svg>
  </nav>
</section>

<!-- Screen: available devices -->
<section class="phone" style="left:626px;top:55px">
  <span class="status-time">9:41</span>
  <svg class="status-icons"><use href="#i-status"/></svg>
  <span class="brand">valkemo</span>
  <div class="top-actions">
    <span class="round-btn"><svg><use href="#i-wifi"/></svg></span>
    <span class="round-btn"><svg><use href="#i-grid"/></svg></span>
    <span class="round-btn" style="color:#222"><svg><use href="#i-user"/></svg></span>
  </div>
  <h1 class="screen-title" style="top:189px">Devices available to connect</h1>
  <div class="device" style="top:214px">Xy timer<span class="switch off"></span></div>
  <div class="device" style="top:250px">IT siren abc<span class="switch off"></span></div>
  <div class="device" style="top:286px">Support team speaker<span class="switch off"></span></div>

  <nav class="tab-bar">
    <span class="active-mark"></span>
    <svg style="left:21px"><use href="#i-home"/></svg>
    <svg style="left:77px"><use href="#i-box"/></svg>
    <svg style="left:140px"><use href="#i-cal"/></svg>
    <svg style="left:196px"><use href="#i-gear"/></svg>
  </nav>
</section>

<!-- Screen: wifi pairing -->
<section class="phone" style="left:908px;top:97px">
  <span class="status-time">9:41</span>
  <svg class="status-icons"><use href="#i-status"/></svg>
  <span class="brand">valkemo</span>
  <div class="top-actions">
    <span class="round-btn"><svg><use href="#i-wifi"/></svg></span>
    <span class="round-btn"><svg><use href="#i-grid"/></svg></span>
    <span class="round-btn" style="color:#222"><svg><use href="#i-user"/></svg></span>
  </div>
  <p class="pair-text">You will be connecting to xy timer<br>to your account using wifi pairing</p>
  <div class="pair-link">
    <span class="pair-node" style="left:0;color:var(--yellow)"><svg><use href="#i-user"/></svg></span>
    <span class="pair-line"></span>
    <span class="pair-node" style="right:0;color:var(--yellow)"><svg><use href="#i-clock"/></svg></span>
  </div>

  <nav class="tab-bar">
    <span class="active-mark"></span>
    <svg style="left:21px"><use href="#i-home"/></svg>
    <svg style="left:77px"><use href="#i-box"/></svg>
    <svg style="left:140px"><use href="#i-cal"/></svg>
    <svg style="left:196px"><use href="#i-gear"/></svg>
  </nav>
</section>

</body>
</html>
```